UI for Online Code Editor

I need a UI design for an online code editor called Quillworth.

Quillworth is an online code editor for web developers, that aims to be an intuitive and beautiful editor that you can use on any device or browser. The current prototype can be viewed at http://quillworth.example/editor

I am completely open to different colours and UI approaches, feel free to invent a new way for people to code :)

The final design should be something that is clean, elegant and functional. I will favour designs that are genuinely nice to look at and have a 'mac app' polished feel to them.

I have uploaded a psd that will provide a basic idea.

Go crazy, All ideas will be considered.

Target Market(s)

Web Developers

Industry/Entity Type

Online

Requirements
Must have
• -Tabs: similar to vantor tabs, for different files.
-Line numbers
-The editor text area
Nice to have
• -An expandable/contractible file manager, on either side of the editor.
-Related files area under tabs. This is for quick access to files that have been included in the users code (ie jquery.js, etc). This will likely be expandable/contractable.

```html
<!DOCTYPE html>
<html lang="en">
<head>
<meta charset="utf-8">
<title>Quillworth Editor</title>
<link rel="stylesheet" href="https://fonts.googleapis.com/css2?family=Arimo:wght@400;700&display=swap">
<style>
:root{
  --bar:#ececec;
  --bar-line:#c9c9c9;
  --accent:#19b9de;
  --panel-head:#dcdcdc;
  --tree-top:#9a9a9a;
  --tree-bottom:#8a8a8a;
  --scroll-track:#7a7a7a;
  --scroll-thumb:#e9e9e9;
  --tabstrip:#8f8f8f;
  --tab:#ececec;
  --pill:#8c8c8c;
  --gutter:#b3b3b3;
  --editor:#404040;
  --text-dark:#555;
  --text-mid:#777;
  --white:#fff;
}
*{margin:0;padding:0;box-sizing:border-box}
html,body{width:1200px;height:663px;overflow:hidden;background:var(--bar)}
body{position:relative;font-family:"Arimo",Arial,sans-serif;color:var(--text-dark)}
.abs{position:absolute}

.toolbar{left:0;top:0;width:1200px;height:68px;background:var(--bar);border-bottom:1px solid var(--bar-line)}
.brand{left:48px;top:20px;display:flex;align-items:center;gap:8px;font-size:25px;color:#3a3a3a}
.brand-mark{width:18px;height:18px;background:var(--accent)}
.divider{top:22px;width:1px;height:24px;background:var(--bar-line)}
.tool-active{left:646px;top:10px;width:70px;height:48px;background:#e2e2e2;border:1px solid #d6d6d6;border-radius:3px}

.sidebar-head{left:0;top:68px;width:223px;height:41px;background:var(--panel-head);border-bottom:1px solid #c4c4c4}
.sidebar-head span{position:absolute;left:47px;top:12px;font-size:15px;color:var(--text-mid)}
.close-btn{width:20px;height:20px;background:#f1f1f1;border:1px solid #bbb;border-radius:2px;display:flex;align-items:center;justify-content:center}
.tree{left:0;top:110px;width:223px;height:512px;background:linear-gradient(var(--tree-top),var(--tree-bottom))}
.scroll-track{left:203px;top:110px;width:20px;height:512px;background:var(--scroll-track)}
.scroll-thumb{left:207px;top:113px;width:12px;height:67px;background:var(--scroll-thumb);border-radius:3px}
.node{font-size:12px;color:var(--white);display:flex;align-items:center;gap:10px;height:20px}
.twisty{width:9px;height:9px;border:1px solid #555;background:#ddd}
.tree-line{background:#555;width:1px}
.sidebar-foot{left:0;top:622px;width:223px;height:41px;background:var(--panel-head);border-top:1px solid #bbb;border-right:1px solid #bbb}
.sidebar-foot span{position:absolute;left:48px;top:12px;font-size:15px;color:var(--text-mid)}

.tabstrip{left:224px;top:68px;width:976px;height:41px;background:var(--tabstrip)}
.tab{left:224px;top:68px;width:190px;height:42px;background:var(--tab)}
.tab span{position:absolute;left:30px;top:14px;font-size:15px;color:var(--text-mid)}
.add-tab{left:421px;top:75px;width:28px;height:27px;background:var(--accent);border-radius:3px}
.related{left:224px;top:110px;width:976px;height:46px;background:var(--tab)}
.pill{left:254px;top:124px;width:113px;height:24px;border-radius:12px;background:var(--pill);border:1px solid #777;color:var(--white);font-size:12px;text-align:center;line-height:22px}
.gutter{left:224px;top:156px;width:30px;height:466px;background:var(--gutter)}
.gutter div{height:23px;line-height:24px;text-align:center;font-size:13px;color:var(--white)}
.editor{left:254px;top:156px;width:946px;height:466px;background:var(--editor);border-bottom:1px solid #6a2a30}
.statusbar{left:224px;top:622px;width:976px;height:41px;background:var(--tab)}
.statusbar p{position:absolute;right:30px;top:14px;font-size:12px;color:#999}
.statusbar b{font-weight:400;color:#444;margin-right:8px}
</style>
</head>
<body>
<header class="abs toolbar">
  <div class="abs brand"><span class="brand-mark"></span>Quillworth</div>
  <div class="abs divider" style="left:223px"></div>
  <svg class="abs" style="left:254px;top:24px" width="27" height="23" viewBox="0 0 27 23"><path d="M1 2h8l2 3h11v4H6L1 21z" fill="var(--accent)"/><path d="M6 10h21l-5 12H1z" fill="var(--accent)"/></svg>
  <svg class="abs" style="left:535px;top:19px" width="46" height="32" viewBox="0 0 46 32"><path d="M18 2L4 16l14 14M28 2l14 14-14 14" stroke="var(--accent)" stroke-width="6" fill="none"/></svg>
  <div class="abs tool-active"></div>
  <svg class="abs" style="left:656px;top:19px" width="50" height="32" viewBox="0 0 50 32"><path d="M18 2L4 16l14 14" stroke="var(--accent)" stroke-width="6" fill="none"/><path d="M29 2l18 14-18 14z" fill="var(--accent)"/></svg>
  <svg class="abs" style="left:793px;top:20px" width="20" height="30" viewBox="0 0 20 30"><path d="M1 1l19 14L1 29z" fill="var(--accent)"/></svg>
  <div class="abs divider" style="left:1114px"></div>
  <svg class="abs" style="left:1147px;top:23px" width="24" height="24" viewBox="0 0 24 24"><g fill="var(--accent)"><circle cx="12" cy="12" r="8"/><rect x="9.5" y="0" width="5" height="24" rx="1"/><rect x="9.5" y="0" width="5" height="24" rx="1" transform="rotate(60 12 12)"/><rect x="9.5" y="0" width="5" height="24" rx="1" transform="rotate(120 12 12)"/></g><circle cx="12" cy="12" r="3.5" fill="var(--bar)"/></svg>
</header>

<aside>
  <div class="abs sidebar-head"><span>Browse files</span><div class="abs close-btn" style="left:191px;top:11px"><svg width="10" height="10"><path d="M1 1l8 8M9 1L1 9" stroke="#888" stroke-width="2"/></svg></div></div>
  <div class="abs tree"></div>
  <div class="abs tree-line" style="left:13px;top:141px;height:347px"></div>
  <div class="abs tree-line" style="left:37px;top:192px;height:26px"></div>

  <div class="abs node" style="left:9px;top:131px"><i class="twisty"></i><svg width="20" height="17"><path d="M0 1h7l2 2h11v14H0z" fill="#eee"/></svg>Folder Name</div>
  <div class="abs node" style="left:9px;top:157px"><i class="twisty"></i><svg width="20" height="17"><path d="M0 1h7l2 2h9v3H4L0 17z" fill="#ddd"/><path d="M4 6h16l-4 11H0z" fill="#f2f2f2"/></svg>Folder Name</div>
  <div class="abs node" style="left:33px;top:182px"><i class="twisty"></i><svg width="20" height="17"><path d="M0 1h7l2 2h11v14H0z" fill="#eee"/></svg>Folder Name</div>
  <div class="abs node" style="left:33px;top:208px"><i class="twisty"></i><svg width="20" height="17"><path d="M0 1h7l2 2h9v3H4L0 17z" fill="#ddd"/><path d="M4 6h16l-4 11H0z" fill="#f2f2f2"/></svg>Folder Name</div>
  <div class="abs node" style="left:74px;top:234px;gap:9px"><svg width="15" height="18"><path d="M0 0h10l5 5v13H0z" fill="#f2f2f2"/></svg>File Name.css</div>
  <div class="abs node" style="left:74px;top:260px;gap:9px"><svg width="15" height="18"><path d="M0 0h10l5 5v13H0z" fill="#f2f2f2"/></svg>File Name.php</div>
  <div class="abs node" style="left:74px;top:288px;gap:9px"><svg width="15" height="18"><path d="M0 0h10l5 5v13H0z" fill="#f2f2f2"/></svg>File Name.css</div>
  <div class="abs node" style="left:74px;top:314px;gap:9px"><svg width="15" height="18"><path d="M0 0h10l5 5v13H0z" fill="#f2f2f2"/></svg>File Name.php</div>
  <div class="abs node" style="left:74px;top:340px;gap:9px"><svg width="15" height="18"><path d="M0 0h10l5 5v13H0z" fill="#f2f2f2"/></svg>File Name.php</div>
  <div class="abs node" style="left:9px;top:366px"><i class="twisty"></i><svg width="20" height="17"><path d="M0 1h7l2 2h11v14H0z" fill="#eee"/></svg>Folder Name</div>
  <div class="abs node" style="left:9px;top:394px"><i class="twisty"></i><svg width="20" height="17"><path d="M0 1h7l2 2h11v14H0z" fill="#eee"/></svg>Folder Name</div>
  <div class="abs node" style="left:9px;top:422px"><i class="twisty"></i><svg width="20" height="17"><path d="M0 1h7l2 2h11v14H0z" fill="#eee"/></svg>Folder Name</div>
  <div class="abs node" style="left:9px;top:450px"><i class="twisty"></i><svg width="20" height="17"><path d="M0 1h7l2 2h11v14H0z" fill="#eee"/></svg>Folder Name</div>
  <div class="abs node" style="left:9px;top:478px"><i class="twisty"></i><svg width="20" height="17"><path d="M0 1h7l2 2h11v14H0z" fill="#eee"/></svg>Folder Name</div>

  <div class="abs scroll-track"></div>
  <div class="abs scroll-thumb"></div>
  <div class="abs sidebar-foot"><span>Global</span><svg class="abs" style="left:99px;top:17px" width="11" height="8"><path d="M0 0h11L5.5 8z" fill="#888"/></svg></div>
</aside>

<main>
  <div class="abs tabstrip"></div>
  <div class="abs tab"><span>Untitled</span><div class="abs close-btn" style="left:157px;top:11px;border-color:#ddd"><svg width="10" height="10"><path d="M1 1l8 8M9 1L1 9" stroke="#bbb" stroke-width="2"/></svg></div></div>
  <div class="abs add-tab"><svg width="28" height="27"><path d="M14 6v15M6.5 13.5h15" stroke="#777" stroke-width="5"/></svg></div>
  <div class="abs related"></div>
  <div class="abs pill">Source Code</div>
  <div class="abs gutter">
    <div>1</div><div>2</div><div>3</div><div>4</div><div>5</div><div>6</div><div>7</div><div>8</div><div>9</div><div>10</div>
    <div>11</div><div>12</div><div>13</div><div>14</div><div>15</div><div>16</div><div>17</div><div>18</div><div>19</div><div>20</div>
  </div>
  <div class="abs editor"></div>
  <footer class="abs statusbar"><p>Row: <b>17</b> Col: <b>14</b> Total: <b style="margin-right:0">356</b></p></footer>
</main>
</body>
</html>
```